Geschäftspapiere für PARVENTO
Zielgruppe
We sell Tee Times online and in real time for golfers
Aufgabenstellung
We need a layout for a voucher, invoice, letterhead.
Especially the voucher should be easily be printable from any customer at home.
The attached voucher is just an example of which informations need to included

```html
<!DOCTYPE html>
<html lang="de">
<head>
<meta charset="utf-8">
<title>PARVENTO – Geschäftspapiere</title>
<link rel="stylesheet" href="https://fonts.googleapis.com/css2?family=Comfortaa:wght@500;700&family=Source+Sans+3:wght@400;600&display=swap">
<style>
  :root {
    --green: #7ea113;
    --green-light: #a9c400;
    --ink: #4a4a4a;
    --ink-soft: #5c5c5c;
    --paper: #ffffff;
    --paper-soft: #f4f4f4;
    --backdrop: #e8e8e8;
  }
  * { box-sizing: border-box; margin: 0; padding: 0; }
  html, body { width: 1200px; height: 1200px; overflow: hidden; background: var(--backdrop); }
  body { font-family: "Source Sans 3", "Source Sans Pro", sans-serif; color: var(--ink); position: relative; }

  .voucher { position: absolute; left: 69px; width: 534px; height: 267px; overflow: hidden; }
  .voucher--green { top: 333px; background: var(--green); color: #fff; }
  .voucher--print { top: 637px; background: var(--paper); }

  .voucher__title {
    position: absolute; left: 28px; top: 26px;
    font-family: "Comfortaa", sans-serif; font-weight: 700;
    font-size: 34px; line-height: 29px; letter-spacing: 0.5px; text-transform: lowercase;
  }
  .voucher__title span { display: block; }
  .voucher__title span + span { padding-left: 26px; }
  .voucher--print .voucher__title { color: var(--green); }

  .voucher__when { position: absolute; left: 63px; top: 108px; font-size: 14px; line-height: 18px; }
  .voucher--print .voucher__when { color: var(--ink); }

  .voucher__course { position: absolute; left: 204px; top: 108px; font-size: 9.5px; line-height: 12.5px; color: var(--ink-soft); }
  .voucher__course h3 { font-weight: 400; font-size: 14px; line-height: 18px; color: var(--green); margin-bottom: 3px; }
  .voucher__course p + p { margin-top: 5px; }

  .voucher__guests { position: absolute; left: 361px; top: 127px; font-size: 9.5px; line-height: 12.5px; color: var(--ink-soft); }
  .voucher__guests p + p { margin-top: 5px; }

  .voucher__footer { position: absolute; left: 54px; top: 236px; width: 420px; font-size: 5.3px; line-height: 7.5px; color: var(--ink-soft); }
  .voucher__footer .voucher__number { position: absolute; right: 0; top: 0; color: var(--green); }

  .letterhead {
    position: absolute; left: 643px; top: 187px; width: 507px; height: 716px;
    background: var(--paper-soft); font-size: 7.5px; line-height: 13px; color: #333;
  }
  .letterhead__brand {
    position: absolute; left: 0; right: 0; top: 74px; text-align: center;
    font-family: "Source Sans 3", sans-serif; font-weight: 600; font-size: 26px;
    letter-spacing: 2px; color: var(--green);
  }
  .letterhead__sender { position: absolute; left: 64px; top: 126px; font-size: 5.5px; line-height: 8px; color: var(--ink-soft); }
  .letterhead__recipient { position: absolute; left: 64px; top: 153px; }
  .letterhead__subject { position: absolute; left: 64px; top: 259px; font-size: 8.5px; text-transform: uppercase; }
  .letterhead__body { position: absolute; left: 64px; top: 305px; width: 290px; }
  .letterhead__body p { margin-bottom: 13px; }
  .letterhead__rule { position: absolute; left: 64px; width: 394px; top: 674px; height: 1px; background: var(--green-light); }
  .letterhead__footer { position: absolute; left: 64px; width: 394px; top: 680px; text-align: center; font-size: 5.3px; line-height: 7.5px; color: var(--ink-soft); }
</style>
</head>
<body>

  <section class="voucher voucher--green" aria-label="Green Fee Voucher, Vorderseite">
    <h2 class="voucher__title"><span>green fee</span><span>voucher</span></h2>
    <div class="voucher__when">
      <p>Date of play 09.02.17</p>
      <p>Time of play 07:15 am</p>
    </div>
  </section>

  <section class="voucher voucher--print" aria-label="Green Fee Voucher, Druckversion">
    <h2 class="voucher__title"><span>green fee</span><span>voucher</span></h2>
    <div class="voucher__when">
      <p>Date of play 09.02.17</p>
      <p>Time of play 07:15 am</p>
    </div>
    <div class="voucher__course">
      <h3>Son Verdal</h3>
      <p>Cami de sa Torre, Km 4,2<br>07609 Llucmajor</p>
      <p>Phone: 0034&nbsp; 971 402 317/-20<br>Fax: 0034&nbsp; 971 402 318<br>E-Mail: info(at)son-verdal.com<br>GPS Koordinaten</p>
    </div>
    <div class="voucher__guests">
      <p>Frau Berta Mustermann<br>Herr Max mustermann</p>
      <p>Kind 1 Mustermann<br>Kind 2 Mustermann</p>
      <p style="margin-top:16px">Germany</p>
    </div>
    <div class="voucher__footer">
      <p>PARVENTO GbR · Lindenweg 14 · 83661 Lenggries · www.parvento.com · bookings@parvento.com · Phone +49 8042 55 18 207</p>
      <p>Please note that the voucher is only valid on the date, time, Golf Course and person mentioned above. Please present this voucher to reception for check-in</p>
      <span class="voucher__number">Voucher N° 17-543</span>
    </div>
  </section>

  <section class="letterhead" aria-label="Briefbogen">
    <div class="letterhead__brand">PARVENTO</div>
    <p class="letterhead__sender">PARVENTO GbR · Lindenweg 14 · 83661 Lenggries</p>
    <address class="letterhead__recipient" style="font-style:normal">
      Musterfirma GmbH<br>Herr Mustermann<br>Eine andere Straße 12<br>51249 Köln
    </address>
    <h2 class="letterhead__subject" style="font-weight:400">Green Fee Voucher</h2>
    <div class="letterhead__body">
      <p style="margin-bottom:19px">Sehr geehrter Herr Mustermann,</p>
      <p>jeder Setzer hat für diesen Zweck immer etwas Blindtext parat. Blindtext ist im Umfang von einigen tausend Anschlägen, der für die »äußerliche« Gestaltung einer Publikation verwendet und dessen Inhalt unwichtig ist. Man setzt ihn oft zum Beispiel in verschiedenen Schriften und Schriftgrößen, um anderen zu zeigen, wie eine bestimmte Schrift wirkt. Oder man montiert auch komplette ganze Seiten mit sinnlosen Streifen von Blindtext, um das spätere Aussehen der Seiten zu simulieren.</p>
      <p style="margin-bottom:32px">Blindtext wird allerdings oft nur für die Teile einer Seite verwendet, die in so kleiner Schrift gesetzt werden, dass sie beim »Überfliegen« ungelesen bleiben. Jeder Setzer hat für diesen Zweck immer etwas Blindtext parat. Blindtext ist Umfang von einigen tausend Anschlägen, der für die »äußerliche« Gestaltung einer Publikation verwendet und dessen Inhalt unwichtig ist.</p>
      <p>Mit freundlichen Grüßen</p>
    </div>
    <div class="letterhead__rule"></div>
    <div class="letterhead__footer">
      <p>PARVENTO GbR · Lindenweg 14 · 83661 Lenggries · www.parvento.com · bookings@parvento.com · Phone +49 8042 55 18 207</p>
      <p>Please note that the voucher is only valid on the date, time, Golf Course and person mentioned above. Please present this voucher to reception for check-in</p>
    </div>
  </section>

</body>
</html>
```